Powerpoint Slide Deck

I had my logo designed using artfolda and would like to have a professional looking powerpoint deck created with my logo etc. my website is brovana.info

```html
<!DOCTYPE html>
<html lang="en">
<head>
<meta charset="utf-8">
<title>Brovana Presentation Deck</title>
<link href="https://fonts.googleapis.com/css2?family=Raleway:wght@300;400;600;700;800&display=swap" rel="stylesheet">
<style>
:root{
  --purple:#5b3fd0;
  --violet:#7d4fc4;
  --orchid:#c07fd0;
  --ink:#3c4247;
  --grey:#6a6a72;
  --light:#f2f2f4;
  --board:#dddde2;
  --white:#ffffff;
  --blue:#5b46d6;
  --magenta:#a44fc8;
  --green:#56c96b;
  --red:#e52a2a;
}
*{margin:0;padding:0;box-sizing:border-box}
html,body{width:798px;height:1200px;overflow:hidden}
body{font-family:"Raleway",sans-serif;background:var(--board);position:relative;color:var(--grey)}
.hero{position:absolute;left:0;top:0;width:798px;height:500px;background:linear-gradient(180deg,#c9cbd3 0%,#e4e4e8 70%,var(--board) 100%)}
.hero-slide{position:absolute;left:40px;top:95px;transform:scale(1.444);transform-origin:0 0;box-shadow:0 10px 30px rgba(40,30,80,.25)}
.hero-brand{position:absolute;left:628px;top:80px;display:flex;align-items:center;gap:8px;font-size:28px;font-weight:600;color:var(--ink);white-space:nowrap}
.dot{width:14px;height:14px;border-radius:50%;background:var(--violet);flex:none}
.hero-brand .dot{width:18px;height:18px}

.slide{position:absolute;width:374px;height:210px;background:var(--white);overflow:hidden}
.s1{left:19px;top:520px}.s2{left:405px;top:520px}
.s3{left:19px;top:743px}.s4{left:405px;top:743px}
.s5{left:19px;top:966px}.s6{left:405px;top:966px}
.abs{position:absolute}

.brand{position:absolute;display:flex;align-items:center;gap:4px;font-weight:600;color:var(--ink);white-space:nowrap}
.brand .dot{width:7px;height:7px}
.brand-lg{font-size:13px}
.brand-sm{font-size:7.5px;left:10px;top:188px}
.brand-sm .dot{width:5px;height:5px}

.band{position:absolute;left:0;top:0;width:374px;height:210px}
.title{position:absolute;left:39px;top:80px;color:var(--white);font-weight:800;font-size:18px;line-height:20px;letter-spacing:.3px}
.subtitle{position:absolute;left:39px;top:124px;color:var(--white);font-size:8px;font-weight:400}
.date{position:absolute;left:39px;top:150px;width:68px;height:12px;border:1px solid var(--white);border-radius:2px;color:var(--white);font-size:4.5px;letter-spacing:1px;font-weight:700;display:flex;align-items:center;justify-content:center}
.copy-center{position:absolute;left:0;width:374px;top:197px;text-align:center;font-size:4px;color:#999}

.footer-bar{position:absolute;left:50px;top:190px;width:314px;height:8px;border-radius:4px;background:linear-gradient(90deg,var(--orchid),var(--purple))}
.footer-bar span{position:absolute;right:14px;top:2px;font-size:3.2px;color:var(--white)}
.footer-bar i{position:absolute;right:1px;top:1px;width:6px;height:6px;border-radius:50%;background:var(--white);font-style:normal;font-size:3.5px;color:var(--purple);text-align:center;line-height:6px;font-weight:700}

.heading{font-size:13px;font-weight:300;color:var(--grey)}
.heading b{font-weight:700}
.body{font-size:6px;line-height:6.8px;color:var(--grey)}
.body p{margin-bottom:3.5px}
.centered{text-align:center;width:374px;left:0}

.sol{position:absolute;top:66px;width:90px;text-align:center}
.sol .ring{width:40px;height:40px;margin:0 auto;border-radius:50%;display:flex;align-items:center;justify-content:center}
.sol h3{font-size:7px;font-weight:400;margin-top:10px}
.sol h3 b,.item h3 b{font-weight:700}
.sol p{font-size:4.3px;line-height:5px;margin-top:7px}
.item{position:absolute;width:80px}
.item h3{font-size:7px;font-weight:400}
.item p{font-size:4.2px;line-height:5px;margin-top:5px}
.item.left{text-align:right;left:46px}
.item.right{text-align:left;left:248px}

.thanks{position:absolute;left:39px;top:58px;font-size:17px;font-weight:300;color:var(--white)}
.contact-h{position:absolute;left:39px;top:103px;font-size:8px;font-weight:700;color:var(--white)}
.contact{position:absolute;left:39px;display:flex;align-items:center;gap:5px;font-size:5.5px;color:var(--white)}
</style>
</head>
<body>

<section class="hero">
  <div class="slide hero-slide">
    <svg class="band" viewBox="0 0 374 210" aria-hidden="true"><defs><linearGradient id="hg" x1="0" x2="1"><stop offset="0" stop-color="#5b3fd0"/><stop offset="1" stop-color="#8a5ec8"/></linearGradient></defs><polygon points="0,53 91,53 129,21 374,21 374,189 0,189" fill="url(#hg)"/></svg>
    <div class="abs" role="img" aria-label="Photo of two IT engineers with a laptop in a server room" style="left:150px;top:21px;width:224px;height:168px;background:linear-gradient(90deg,rgba(91,63,208,0),rgba(150,120,220,.45))"></div>
    <div class="brand brand-lg" style="left:26px;top:30px"><span class="dot"></span>Brovana</div>
    <div class="title">PRESENTATION<br>TITLE GOES HERE!</div>
    <div class="subtitle">Sub Title of Presentation Goes Here</div>
    <div class="date">February 16, 2023</div>
    <div class="copy-center">Copyright © 2022 Brovana All rights reserved</div>
  </div>
  <div class="hero-brand"><span class="dot"></span>Brovana</div>
</section>

<!-- Title slide -->
<section class="slide s1">
  <svg class="band" viewBox="0 0 374 210" aria-hidden="true"><defs><linearGradient id="g1" x1="0" x2="1"><stop offset="0" stop-color="#5b3fd0"/><stop offset="1" stop-color="#8a5ec8"/></linearGradient></defs><polygon points="0,53 91,53 129,21 374,21 374,189 0,189" fill="url(#g1)"/></svg>
  <div class="abs" role="img" aria-label="Photo of two IT engineers with a laptop in a server room" style="left:150px;top:21px;width:224px;height:168px;background:linear-gradient(90deg,rgba(91,63,208,0),rgba(150,120,220,.45))"></div>
  <div class="brand brand-lg" style="left:26px;top:30px"><span class="dot"></span>Brovana</div>
  <div class="title">PRESENTATION<br>TITLE GOES HERE!</div>
  <div class="subtitle">Sub Title of Presentation Goes Here</div>
  <div class="date">February 16, 2023</div>
  <div class="copy-center">Copyright © 2022 Brovana All rights reserved</div>
</section>

<!-- About -->
<section class="slide s2">
  <div class="abs" role="img" aria-label="Illustration of a team working around a large laptop with code and cloud icons" style="left:25px;top:37px;width:160px;height:120px;border-radius:6px;background:linear-gradient(135deg,#eaf1fb,#cfe0f7)"></div>
  <div class="abs heading" style="left:200px;top:52px"><span style="display:inline-block;width:8px;height:8px;border-radius:50%;background:var(--violet);margin-right:5px"></span>About <b>Brovana</b></div>
  <div class="abs body" style="left:202px;top:85px;width:138px">
    <p>In a complex world of IT, Brovana will assist you in optimizing IT spend. Our 20 plus years in the IT industry brings best of breed personnel from Data center, Managed Services, and Disaster Recovery, to help you get the best solutions for the best price.</p>
    <p>Let us help you simplify.</p>
  </div>
  <div class="brand brand-sm"><span class="dot"></span>Brovana</div>
  <div class="footer-bar"><span>Copyright © 2022 Brovana All rights reserved</span><i>2</i></div>
</section>

<!-- Why -->
<section class="slide s3">
  <div class="abs heading" style="left:37px;top:38px"><span style="display:inline-block;width:8px;height:8px;border-radius:50%;background:var(--violet);margin-right:5px"></span>Why <b>Brovana</b></div>
  <div class="abs body" style="left:40px;top:70px;width:196px">
    <p>It's Simple. Our resources have years of experience understanding IT environments. All of our staff have been top of their class in each of their specialties and can help you optimize your spend with best of breed solutioning.</p>
    <p>Our staff have unmatched knowledge in Networking, Security, Data Center, Disaster Recovery, Keltrona Solutions, Hyperscaler Solutions, Managed Services, and more. The people we put in front of you are the best of the best in IT.</p>
    <p>Its hard to find a great mechanic that you trust has your best interests in mind – its even harder to find a great IT specialist.</p>
    <p>Let our team help you optimize your environment.</p>
  </div>
  <div class="abs" role="img" aria-label="Photo of a desk with a computer monitor, coffee mug, calculator and hands typing" style="left:253px;top:0;width:84px;height:168px;background:linear-gradient(180deg,#dfe3ea,#8a7a68 70%,#4a4038)"></div>
  <div class="brand brand-sm"><span class="dot"></span>Brovana</div>
  <div class="footer-bar"><span>Copyright © 2022 Brovana All rights reserved</span><i>3</i></div>
</section>

<!-- Solutions -->
<section class="slide s4">
  <div class="abs heading centered" style="top:18px">Our <b>Solutions</b></div>
  <div class="sol" style="left:40px">
    <div class="ring" style="background:var(--blue)"><svg width="18" height="12" viewBox="0 0 18 12"><path d="M4 11h10a3.5 3.5 0 0 0 0-7 5 5 0 0 0-9.5 1A3 3 0 0 0 4 11z" fill="#fff"/></svg></div>
    <h3><b>Heading</b> Goes Here</h3>
    <p>Lorem ipsum dolor sit amet, consectetur adipiscing elit. Vivamus eu dui ex. Curabitur dapibus dignissim dui, in molestie metus feugiat sed.</p>
  </div>
  <div class="sol" style="left:142px">
    <div class="ring" style="background:var(--magenta)"><svg width="16" height="12" viewBox="0 0 16 12"><rect x="2" y="1" width="12" height="8" rx="1" fill="none" stroke="#fff" stroke-width="1.5"/><rect x="0" y="10" width="16" height="1.5" fill="#fff"/></svg></div>
    <h3><b>Heading</b> Goes Here</h3>
    <p>Lorem ipsum dolor sit amet, consectetur adipiscing elit. Vivamus eu dui ex. Curabitur dapibus dignissim dui, in molestie metus feugiat sed.</p>
  </div>
  <div class="sol" style="left:244px">
    <div class="ring" style="background:var(--red)"><svg width="14" height="14" viewBox="0 0 14 14"><circle cx="7" cy="7" r="5" fill="none" stroke="#fff" stroke-width="2.4" stroke-dasharray="2 1.4"/><circle cx="7" cy="7" r="2" fill="#fff"/></svg></div>
    <h3><b>Heading</b> Goes Here</h3>
    <p>Lorem ipsum dolor sit amet, consectetur adipiscing elit. Vivamus eu dui ex. Curabitur dapibus dignissim dui, in molestie metus feugiat sed.</p>
  </div>
  <div class="brand brand-sm"><span class="dot"></span>Brovana</div>
  <div class="footer-bar"><span>Copyright © 2022 Brovana All rights reserved</span><i>4</i></div>
</section>

<!-- Cycle -->
<section class="slide s5">
  <div class="abs heading centered" style="top:16px"><b>Heading</b> Goes Here</div>
  <svg class="abs" style="left:0;top:0" width="374" height="210" viewBox="0 0 374 210" aria-hidden="true">
    <circle cx="187" cy="112" r="55" fill="none" stroke="#9a9aa4" stroke-width=".6" stroke-dasharray="2 2"/>
    <circle cx="187" cy="112" r="35" fill="#f1f1f3"/>
    <circle cx="150" cy="74" r="11" fill="var(--blue)" stroke="#fff" stroke-width="2"/>
    <circle cx="224" cy="74" r="11" fill="var(--magenta)" stroke="#fff" stroke-width="2"/>
    <circle cx="150" cy="150" r="11" fill="var(--green)" stroke="#fff" stroke-width="2"/>
    <circle cx="224" cy="150" r="11" fill="var(--red)" stroke="#fff" stroke-width="2"/>
    <circle cx="150" cy="73" r="3" fill="#fff"/><rect x="148.5" y="76" width="3" height="3" fill="#fff"/>
    <circle cx="224" cy="74" r="4" fill="none" stroke="#fff" stroke-width="1.8" stroke-dasharray="1.5 1"/>
    <path d="M146 153h8a2.5 2.5 0 0 0 0-5 3.6 3.6 0 0 0-7 .8A2.2 2.2 0 0 0 146 153z" fill="#fff"/>
    <rect x="219" y="146" width="10" height="6.5" rx=".8" fill="none" stroke="#fff" stroke-width="1.2"/><rect x="218" y="153.5" width="12" height="1.2" fill="#fff"/>
    <text x="187" y="115" text-anchor="middle" font-family="Raleway, sans-serif" font-size="9" font-weight="600" fill="#3c4247">Brovana</text>
  </svg>
  <div class="item left" style="top:62px"><h3><b>Heading</b> Goes Here</h3><p>Adipiscing Elit. Vivamus Eu Dui Ex. Curabitur Dapibus Dignissim Dui, In Molestie Metus Feugiat Sed.</p></div>
  <div class="item right" style="top:62px"><h3><b>Heading</b> Goes Here</h3><p>Adipiscing Elit. Vivamus Eu Dui Ex. Curabitur Dapibus Dignissim Dui, In Molestie Metus Feugiat Sed.</p></div>
  <div class="item left" style="top:136px"><h3><b>Heading</b> Goes Here</h3><p>Adipiscing Elit. Vivamus Eu Dui Ex. Curabitur Dapibus Dignissim Dui, In Molestie Metus Feugiat Sed.</p></div>
  <div class="item right" style="top:136px"><h3><b>Heading</b> Goes Here</h3><p>Adipiscing Elit. Vivamus Eu Dui Ex. Curabitur Dapibus Dignissim Dui, In Molestie Metus Feugiat Sed.</p></div>
  <div class="brand brand-sm"><span class="dot"></span>Brovana</div>
  <div class="footer-bar"><span>Copyright © 2022 Brovana All rights reserved</span><i>5</i></div>
</section>

<!-- Thank you -->
<section class="slide s6">
  <svg class="band" viewBox="0 0 374 210" aria-hidden="true"><defs><linearGradient id="g6" x1="0" x2="1"><stop offset="0" stop-color="#5b3fd0"/><stop offset="1" stop-color="#8a5ec8"/></linearGradient></defs><polygon points="0,21 279,21 300,53 374,53 374,189 0,189" fill="url(#g6)"/></svg>
  <div class="abs" role="img" aria-label="Photo looking up at glass office towers" style="left:160px;top:21px;width:214px;height:168px;clip-path:polygon(0 0,119px 0,140px 32px,100% 32px,100% 100%,0 100%);background:linear-gradient(120deg,rgba(91,63,208,0),rgba(170,140,225,.4))"></div>
  <div class="brand brand-lg" style="left:304px;top:30px"><span class="dot"></span>Brovana</div>
  <div class="thanks">THANK YOU!</div>
  <div class="contact-h">Contact Us</div>
  <div class="contact" style="top:118px"><svg width="7" height="7" viewBox="0 0 10 10"><path d="M2 1l2 2-1 1.5a6 6 0 0 0 2.5 2.5L7 6l2 2-1.5 1.5C4 9 1 6 .5 2.5z" fill="#fff"/></svg>Phone Number Goes Here</div>
  <div class="contact" style="top:129px"><svg width="7" height="7" viewBox="0 0 10 10"><circle cx="5" cy="5" r="4" fill="none" stroke="#fff" stroke-width="1.2"/><circle cx="5" cy="5" r="1.6" fill="none" stroke="#fff" stroke-width="1.2"/></svg>E-Mail Address Goes Here</div>
  <div class="contact" style="top:140px"><svg width="7" height="7" viewBox="0 0 10 10"><circle cx="5" cy="5" r="4" fill="none" stroke="#fff"/><ellipse cx="5" cy="5" rx="1.8" ry="4" fill="none" stroke="#fff"/><path d="M1 5h8" stroke="#fff"/></svg>URL Address Goes Here</div>
  <div class="copy-center">Copyright © 2022 Brovana All rights reserved</div>
</section>

</body>
</html>
```